Great Opportunity !! Masters in Business Analytics College Course

the size is Full Page, with bleed*
8”x 10.75" plus 0.25" bleed.
please leave one inch for footer
the purpose is attract students to join this college program .
this is for students in USA .
college age of around 24 years old
I am looking for a flyer that is unique and shows creativity .
A flyer that people would want to look at it because it is unique.
you can choose either vector, text ,or picture.
if you do picture it should be a white USA citizen wearing a white solid shirt and not long hair

Target Market(s)

USA students about 23 in age to join this college program

Industry/Entity Type

education

Colors
0054AA
0677BA
7BADD7
CADEEF
E8F1F8
0094D4
00A9DD
6FCCEA
C7EBF8
E9F6FB

Requirements
Must have
• the text should not be crowded .. .. .. the ad should not be full of text
Should not have
• not have very large text .. it should not be a flyer that is full of text .. you have to figure out how to avoid looking at the ad and it is very busy with text

```html
<!DOCTYPE html>
<html lang="en">
<head>
<meta charset="utf-8">
<title>Master's in Business Analytics – Info Session Flyer</title>
<link rel="stylesheet" href="https://fonts.googleapis.com/css2?family=Bebas+Neue&family=Montserrat:wght@700;800&family=Open+Sans:wght@400;600&family=Roboto+Condensed:wght@600&display=swap">
<style>
  :root {
    --blue-deep: #0054AA;
    --blue-mid: #0677BA;
    --blue-bright: #0094D4;
    --cyan: #00A9DD;
    --navy: #2A4478;
    --banner-fold: #2B4A86;
    --envelope-back: #1552A8;
    --envelope-front-a: #0B62B6;
    --envelope-front-b: #0A7AC2;
    --envelope-shade: #1257AD;
    --ink: #111111;
    --paper: #FFFFFF;
    --page-bg: #FFFFFF;
  }
  html, body {
    margin: 0;
    padding: 0;
    width: 1200px;
    height: 1200px;
    overflow: hidden;
    background: var(--page-bg);
  }
  .canvas {
    position: relative;
    width: 1200px;
    height: 1200px;
  }
  .flyer {
    position: absolute;
    left: 200px;
    top: 34px;
    width: 800px;
    height: 1131px;
    display: block;
  }
  .banner-text {
    font-family: "Bebas Neue", "Oswald", sans-serif;
    fill: var(--paper);
    font-size: 58px;
  }
  .program-title {
    font-family: "Montserrat", sans-serif;
    font-weight: 800;
    font-size: 30px;
    fill: var(--cyan);
  }
  .school-name {
    font-family: "Montserrat", sans-serif;
    font-weight: 800;
    font-size: 30px;
    fill: var(--ink);
  }
  .salary-line {
    font-family: "Montserrat", sans-serif;
    font-weight: 700;
    font-size: 23px;
    fill: var(--blue-deep);
  }
  .source-note {
    font-family: "Open Sans", sans-serif;
    font-size: 22px;
    fill: var(--ink);
  }
  .job-title {
    font-family: "Bebas Neue", "Oswald", sans-serif;
    font-size: 46px;
    fill: var(--cyan);
  }
  .tick-box { fill: none; stroke: var(--ink); stroke-width: 4; }
  .tick-mark { fill: none; stroke: var(--ink); stroke-width: 6; stroke-linecap: round; stroke-linejoin: round; }
  .employers {
    font-family: "Open Sans", sans-serif;
    font-weight: 600;
    font-size: 23px;
    fill: var(--ink);
  }
  .event-box { fill: var(--navy); }
  .event-date {
    font-family: "Montserrat", sans-serif;
    font-weight: 800;
    font-size: 31px;
    fill: var(--paper);
  }
  .event-contact {
    font-family: "Open Sans", sans-serif;
    font-size: 20px;
    fill: var(--paper);
  }
  .accreditation {
    font-family: "Roboto Condensed", sans-serif;
    font-weight: 600;
    font-size: 18px;
    fill: var(--ink);
  }
  .format-line {
    font-family: "Montserrat", sans-serif;
    font-weight: 700;
    font-size: 27px;
    fill: var(--blue-mid);
  }
  .dotted-rule {
    stroke: var(--blue-mid);
    stroke-width: 4;
    stroke-dasharray: 3 4.2;
  }
</style>
</head>
<body>
<main class="canvas">
  <svg class="flyer" viewBox="0 0 1047 1480" xmlns="http://www.w3.org/2000/svg" aria-label="Master's in Business Analytics information session flyer">
    <defs>
      <linearGradient id="photoTone" x1="0" y1="0" x2="0" y2="1">
        <stop offset="0" stop-color="#C9BFA8"/>
        <stop offset="0.35" stop-color="#B7B59A"/>
        <stop offset="0.6" stop-color="#8FAE6C"/>
        <stop offset="0.85" stop-color="#C6D3B4"/>
        <stop offset="1" stop-color="#FFFFFF"/>
      </linearGradient>
      <linearGradient id="envelopeFront" x1="0" y1="0" x2="1" y2="0">
        <stop offset="0" stop-color="var(--envelope-front-a)"/>
        <stop offset="1" stop-color="var(--envelope-front-b)"/>
      </linearGradient>
      <linearGradient id="cardTopShade" x1="0" y1="0" x2="0" y2="1">
        <stop offset="0" stop-color="#FFFFFF"/>
        <stop offset="1" stop-color="#DADADA"/>
      </linearGradient>
      <filter id="cardShadow" x="-10%" y="-10%" width="120%" height="120%">
        <feDropShadow dx="0" dy="0" stdDeviation="10" flood-color="#000" flood-opacity="0.35"/>
      </filter>
    </defs>

    <!-- page -->
    <rect class="page" x="0" y="0" width="1047" height="1480" fill="var(--paper)"/>

    <!-- hero photo area -->
    <rect class="hero-photo" x="0" y="0" width="1047" height="600" fill="url(#photoTone)" role="img" aria-label="Photo: two college students reading a book together on a campus lawn, with other students walking in front of a brick building"/>

    <!-- headline banners -->
    <g class="headline-banners">
      <polygon class="banner-fold" points="188,557 798,458 828,460 683,505 188,557" fill="var(--banner-fold)"/>
      <polygon class="banner banner-one" points="76,425 820,360 828,460 78,523" fill="var(--blue-deep)"/>
      <text class="banner-text" transform="translate(103,497) rotate(-5)" textLength="700" lengthAdjust="spacingAndGlyphs">DO YOU HAVE AN ANALYTICAL MIND?</text>
      <polygon class="banner banner-two" points="176,557 921,485 925,583 185,655" fill="var(--blue-deep)"/>
      <text class="banner-text" transform="translate(201,624) rotate(-5.3)" textLength="710" lengthAdjust="spacingAndGlyphs">ARE YOU SEEKING A PROFITABLE CAREER?</text>
    </g>

    <!-- program pitch -->
    <g class="program-pitch" text-anchor="middle">
      <text class="program-title" x="529" y="691" textLength="625" lengthAdjust="spacingAndGlyphs">A MASTER'S IN BUSINESS ANALYTICS-</text>
      <text class="school-name" x="529" y="730" textLength="552" lengthAdjust="spacingAndGlyphs">RIDGEVIEW STATE UNIVERSITY **</text>
      <text class="salary-line" x="529" y="793" textLength="642" lengthAdjust="spacingAndGlyphs">CAN PREPARE YOU FOR IN-DEMAND JOBS WITH A</text>
      <text class="salary-line" x="529" y="822">MEDIAN SALARY OF $100K+</text>
      <text class="source-note" x="521" y="851">(the National Labor Data Office 2023)</text>
    </g>

    <!-- envelope back -->
    <polygon class="envelope-back" points="0,1100 61,1080 987,1080 1047,1100 1047,1480 0,1480" fill="var(--envelope-back)"/>

    <!-- info card -->
    <rect class="card-top-shade" x="20" y="858" width="1007" height="40" rx="20" fill="url(#cardTopShade)"/>
    <rect class="info-card" x="61" y="893" width="926" height="587" fill="var(--paper)" filter="url(#cardShadow)"/>

    <g class="career-paths">
      <g class="career-item">
        <rect class="tick-box" x="126" y="940" width="30" height="26" rx="3"/>
        <polyline class="tick-mark" points="133,952 141,962 160,936"/>
        <text class="job-title" x="171" y="972" textLength="202" lengthAdjust="spacingAndGlyphs">BI DEVELOPER</text>
      </g>
      <g class="career-item">
        <rect class="tick-box" x="398" y="940" width="30" height="26" rx="3"/>
        <polyline class="tick-mark" points="405,952 413,962 432,936"/>
        <text class="job-title" x="443" y="972" textLength="208" lengthAdjust="spacingAndGlyphs">DATA ANALYST</text>
      </g>
      <g class="career-item">
        <rect class="tick-box" x="679" y="940" width="30" height="26" rx="3"/>
        <polyline class="tick-mark" points="686,952 694,962 713,936"/>
        <text class="job-title" x="721" y="972" textLength="227" lengthAdjust="spacingAndGlyphs">DATA SCIENTIST</text>
      </g>
      <text class="employers" x="520" y="1004" text-anchor="middle" textLength="683" lengthAdjust="spacingAndGlyphs">GRADUATES WERE HIRED AT: CORVELL, BRANDT &amp; LOWE, NEXATEC, VOLTREX</text>
    </g>

    <g class="event-details" text-anchor="middle">
      <rect class="event-box" x="258" y="1036" width="524" height="103"/>
      <text class="event-date" x="520" y="1085" textLength="408" lengthAdjust="spacingAndGlyphs">WED., APRIL 20, 7:30 PM.</text>
      <text class="event-contact" x="520" y="1111" textLength="412" lengthAdjust="spacingAndGlyphs">EMAIL FOR LINK  ALEXMORGAN@GRADMAIL.COM</text>
      <text class="accreditation" x="527" y="1163" textLength="704" lengthAdjust="spacingAndGlyphs">*** GBSA Accreditation. This distinction is held by only 5% of business schools globally.</text>
    </g>

    <!-- envelope front flap -->
    <polygon class="envelope-front" points="0,1120 505,1317 521,1303 537,1317 1047,1125 1047,1480 0,1480" fill="url(#envelopeFront)"/>
    <polygon class="envelope-shade" points="273,1480 521,1320 778,1480" fill="var(--envelope-shade)" opacity="0.8"/>

    <g class="session-format" text-anchor="middle">
      <text class="format-line" x="523" y="1216" textLength="471" lengthAdjust="spacingAndGlyphs">HYBRID / ONE WEEKLY SESSION</text>
      <line class="dotted-rule" x1="407" y1="1265" x2="640" y2="1265"/>
    </g>
  </svg>
</main>
</body>
</html>
```